Pale Ridge Wine Labels

Pale Ridge is an ultra-premium, allocation-only Napa Valley wine brand being built with one objective: to become a long-term cult collectible.

This is not a retail wine.
This is not a lifestyle brand.
This is not driven by marketing trends.

Production is intentionally limited. Access is controlled through private membership. Every decision—from vineyard sourcing to packaging—is made with long-term brand equity in mind.
We are looking for a label system that reflects that level of discipline.

Design a cult-level wine label system for Pale Ridge that communicates rarity, restraint, and authority at a glance.

This is not decorative Napa.
This must feel like it belongs next to Lanternfield, Dorsett, Quillbrook—and still stand apart.
Brand Positioning
Ultra-premium, allocation-only Napa wine
Private membership model (not retail-driven)
Production capped intentionally (scarcity is real, not marketing)
Designed to become a long-term collectible

Tone:

Controlled
Intentional
Confident
Understated power

If it feels “designed” or “trying”—it’s wrong.

Core Product Structure

You are designing a system, not a single label.

Foundation Wines:

Cabernet Sauvignon (primary SKU)
Signature Blend

Extensions (future / limited):

Limited Edition Blend (art-driven)
Reserve (ultra minimal, elevated version)
Creative Direction (Critical)

We are pursuing cult minimalism with tension.

Think:

Silence > noise
Precision > decoration
Material > graphics

This should feel:

Like it was inevitable, not created
Recognizable from across the room
Memorable after one exposure
Design Constraints

These are non-negotiable:

Bottle: Vetrelle Ostana (tall, powerful silhouette)
Glass: Deep antique green (near black)
Capsule: Matte black (baseline)
Front must work with:
Direct glass etching (ghost etch) OR
Minimal premium paper label

No loud colors.
No trendy typography.
No illustrative storytelling.

Brand Elements to Use
Primary mark: VII (Roman numeral 9)
Brand name: PALE RIDGE
Vintage (subtle, not dominant)

Optional concept element:

Varietal composition expressed as a refined system (e.g., “85 · 15” or structured numeric expression)
Design Goals

Your design should achieve:

Instant Recognition
Must be identifiable from 10 feet away
Tactile Value
Feels expensive before you touch it
Even better once you do
Aging Power
This must still look relevant in 20 years
System Cohesion
Cabernet and Blend must feel like a family
Not two separate brands
What We Are NOT Looking For

Avoid immediately:

Gold foil overload
Script fonts / calligraphy
Illustrated vineyards / animals / crests
Trendy “modern winery” aesthetics
Busy compositions
Obvious luxury clichés

If it looks like:

A Napa tasting room brand → reject
A startup wine brand → reject
Something you'd see on a grocery shelf → reject
Creative Territories to Explore

Designers should explore distinct directions, not minor variations:

Pure Etch Minimalism
VII only
Extremely subtle, almost invisible
Power through absence
Architectural Typography
Strong, controlled use of PALE RIDGE
Spatial tension, alignment-driven
Symbol + System
VII + numeric composition (85 / 15, etc.)
Feels like a formula, not decoration
Material-Driven Label
Paper, emboss, deboss, letterpress
Texture carries the design

Target Market(s)

Ultra-high-net-worth individuals, collectors, and allocation-driven wine buyers. Men and women 35–65 Entrepreneurs, executives, investors Already purchasing cult Napa wines ($250–$1,000+ per bottle) Psychographics: Value scarcity over availability Prefer private access over retail Buy for status, cellar, and long-term collection Appreciate restraint, not flash If it appeals to mass retail, it’s wrong.

Industry/Entity Type

Luxury Wine / Fine Wine / Ultra-Premium Consumer Goods

Requirements
Must have
• 1. Lanternfield Why it matters: True cult positioning Feels rare, quiet, and collector-driven What to take: Effortless authority Doesn’t try to look expensive—it just is Strong identity without noise What to avoid: Do not replicate illustration or vintage storytelling style 2. Quillbrook (Dorsett Family) Why it matters: Masterclass in restraint and architectural design What to take: Minimalism with structure Precision typography and spacing Confidence through reduction What to avoid: Don’t make it cold or overly corporate 3. Dorsett Estate Why it matters: One of the most iconic luxury wine labels ever What to take: Timelessness Balance of tradition + authority Label presence without excess What to avoid: Avoid classic/heritage clichés (crests, shields, etc.) 4. Tacet Duo Why it matters: Instantly recognizable globally Clean, iconic silhouette and branding system What to take: Immediate recognition from distance Cohesive system across vintages What to avoid: Don’t go mainstream or overly commercial 5. Hollow Falcon Why it matters: Pure scarcity-driven brand power What to take: Understated exclusivity Nothing feels added for effect What to avoid: Do not introduce illustration or narrative-driven visuals

```html
<!DOCTYPE html>
<html lang="en">
<head>
<meta charset="utf-8">
<title>Pale Ridge — Cabernet Sauvignon Label</title>
<link rel="stylesheet" href="https://fonts.googleapis.com/css2?family=Cormorant+Garamond:wght@500;600&display=swap">
<style>
  :root {
    --page: #ffffff;
    --glass-deep: #1e2410;
    --glass-mid: #262d12;
    --glass-edge: #2b2e26;
    --silver: #e9e9e6;
    --silver-soft: #cfcfcc;
    --panel-light: #f4f4f2;
    --panel-shade: #c9c9c7;
    --mark: #1f2a06;
  }
  * { margin: 0; padding: 0; box-sizing: border-box; }
  html, body {
    width: 1200px;
    height: 750px;
    overflow: hidden;
    background: var(--page);
  }
  body {
    display: flex;
    align-items: center;
    justify-content: center;
    font-family: "Cormorant Garamond", Georgia, serif;
  }
  .label {
    width: 470px;
    height: 700px;
    background: linear-gradient(90deg, var(--glass-edge) 0%, var(--glass-deep) 30%, var(--glass-mid) 55%, var(--glass-deep) 75%, var(--glass-edge) 100%);
    display: flex;
    flex-direction: column;
    align-items: center;
    padding-top: 54px;
    color: var(--silver);
  }
  .brand-name {
    font-size: 42px;
    font-weight: 500;
    letter-spacing: 1px;
    line-height: 1;
  }
  .brand-line {
    margin-top: 8px;
    font-size: 15px;
    font-weight: 500;
    letter-spacing: 9px;
    padding-left: 9px;
    text-transform: uppercase;
  }
  .frame {
    margin-top: 58px;
    width: 300px;
    height: 420px;
    border: 2px solid var(--silver);
    padding: 12px;
  }
  .frame-panel {
    width: 100%;
    height: 100%;
    background: linear-gradient(115deg, var(--panel-shade) 0%, #dcdcda 40%, var(--panel-light) 70%, #e6e6e4 100%);
    display: flex;
    align-items: center;
    justify-content: center;
  }
  .mark-name {
    font-size: 120px;
    font-weight: 600;
    color: var(--mark);
    letter-spacing: 2px;
    line-height: 1;
  }
  .varietal {
    margin-top: 52px;
    font-size: 25px;
    font-weight: 500;
    letter-spacing: 0.5px;
    line-height: 1;
  }
  .vintage {
    margin-top: 14px;
    font-size: 19px;
    font-weight: 500;
    color: var(--silver-soft);
    line-height: 1;
  }
</style>
</head>
<body>
  <main class="label">
    <h1 class="brand-name">PALE RIDGE</h1>
    <p class="brand-line">Signature Blend</p>
    <div class="frame">
      <div class="frame-panel">
        <span class="mark-name">VII</span>
      </div>
    </div>
    <p class="varietal">CABERNET SAUVIGNON</p>
    <p class="vintage">2006</p>
  </main>
</body>
</html>
```